Refresh of The Marston Collective business card

Update business card design using existing primary logo. Names, numbers, etc. are too hard to read on current design.

Target Market(s)

We are a CPA firm.

Industry/Entity Type

Accountant

Contact Information for Business Card

update current card

Colors
0355a3
3176b5
85acd3
0792cd

Requirements
Must have
• Easier to read phone numbers and names
• Use existing logo
Nice to have
• We love our color scheme and current TMC logo. But the names and phone numbers are too small and card just look old and stale.

```html
<!DOCTYPE html>
<html lang="en">
<head>
<meta charset="utf-8">
<title>Daniel R. Ashby, CPA — Business Card</title>
<link href="https://fonts.googleapis.com/css2?family=Lato:ital,wght@0,400;0,700;1,400;1,900&display=swap" rel="stylesheet">
<style>
  :root {
    --stage: #e6e2da;
    --paper: #f3f3f3;
    --ink-dark: #1b1b1c;
    --ink-dark-2: #2a2a2b;
    --brand-navy: #0355a3;
    --brand-blue: #3176b5;
    --brand-sky: #85acd3;
    --brand-cyan: #0792cd;
    --text-light: #eeeeee;
    --text-muted: #d8d8d8;
  }
  * { margin: 0; padding: 0; box-sizing: border-box; }
  html, body {
    width: 1200px; height: 900px; overflow: hidden;
    background: var(--stage);
    font-family: "Lato", Arial, sans-serif;
  }
  .card {
    position: absolute; left: 75px; top: 150px;
    width: 1050px; height: 600px;
    background: var(--paper);
    overflow: hidden;
    box-shadow: 0 10px 30px rgba(0,0,0,0.18);
  }
  .brand {
    position: absolute; left: 300px; top: 90px;
    display: flex; align-items: center; gap: 16px;
  }
  .brand__mark {
    width: 40px; height: 40px; flex: none;
    background: var(--brand-cyan);
  }
  .brand__name {
    color: var(--brand-navy); font-weight: 700;
    font-size: 34px; letter-spacing: 0.5px; white-space: nowrap;
  }
  .card__lower {
    position: absolute; left: 0; right: 0; top: 255px; bottom: 0;
    background: linear-gradient(160deg, var(--ink-dark-2), var(--ink-dark) 60%);
  }
  .name-band {
    position: absolute; left: 0; top: 205px;
    width: 560px; height: 50px;
    background: var(--brand-navy);
    display: flex; align-items: center; justify-content: flex-end;
    padding-right: 18px;
  }
  .name-band__name {
    color: #fff; font-weight: 900; font-style: italic;
    font-size: 30px; letter-spacing: 1.5px; text-transform: uppercase;
    white-space: nowrap;
  }
  .title {
    position: absolute; left: 0; top: 264px; width: 542px;
    text-align: right; color: var(--brand-sky);
    font-style: italic; font-size: 17px; letter-spacing: 0.6px;
    text-transform: uppercase;
  }
  .contacts {
    position: absolute; left: 290px; top: 360px;
    display: grid; row-gap: 18px;
    color: var(--text-light); font-size: 22px; letter-spacing: 0.4px;
  }
  .contacts__row { display: flex; gap: 34px; }
  .contact { display: flex; align-items: center; gap: 14px; white-space: nowrap; }
  .contact__marker { width: 14px; height: 16px; flex: none; }
  .contact__marker polygon { fill: var(--brand-cyan); }
  .contact--address { text-transform: uppercase; font-size: 21px; }
</style>
</head>
<body>
  <div class="card">
    <div class="brand">
      <span class="brand__mark"></span>
      <span class="brand__name">The Marston Collective</span>
    </div>
    <div class="card__lower"></div>
    <div class="name-band"><span class="name-band__name">Daniel R. Ashby, CPA</span></div>
    <div class="title">Certified Public Accountants</div>

    <div class="contacts">
      <div class="contacts__row">
        <div class="contact"><svg class="contact__marker" viewBox="0 0 14 16"><polygon points="0,0 14,8 0,16"/></svg>danr@themarstoncollective.com</div>
        <div class="contact"><svg class="contact__marker" viewBox="0 0 14 16"><polygon points="0,0 14,8 0,16"/></svg>www.themarstoncollective.com</div>
      </div>
      <div class="contacts__row">
        <div class="contact"><svg class="contact__marker" viewBox="0 0 14 16"><polygon points="0,0 14,8 0,16"/></svg>555.201.4410</div>
        <div class="contact"><svg class="contact__marker" viewBox="0 0 14 16"><polygon points="0,0 14,8 0,16"/></svg>555.318.2276</div>
        <div class="contact"><svg class="contact__marker" viewBox="0 0 14 16"><polygon points="0,0 14,8 0,16"/></svg>555.640.9183</div>
      </div>
      <div class="contacts__row">
        <div class="contact contact--address"><svg class="contact__marker" viewBox="0 0 14 16"><polygon points="0,0 14,8 0,16"/></svg>814 W. Harlow Rd. Suite 112 Linwood, Ohio 45601</div>
      </div>
    </div>
  </div>
</body>
</html>
```